Town Planning business needs a design (template) for planning reports and letters

I'm looking to develop a report and a letter template. I prepare town planning reports in NSW, Australia. Fairly straight forward reports which would include figures and tables. I can provide examples of similar reports. I have a logo design which I can also provide ( I have attached one file).

Target Market(s)

Professionals, local and state governments

Industry/Entity Type

Property Development

Requirements
Must have
• Title page, contents, 3 - 4 levels of headings, tables and ability to inset figures/photos and Annexure pages at end of report
Nice to have
• Ability to include short details of project in header or footer

```html
<!DOCTYPE html>
<html lang="en">
<head>
<meta charset="utf-8">
<title>Fieldline Planning — Letterhead</title>
<link rel="stylesheet" href="https://fonts.googleapis.com/css2?family=Jost:wght@400;500&family=Montserrat:wght@700&display=swap">
<style>
  :root {
    --canvas: #ececec;
    --paper: #fdfdfd;
    --ink: #1c1d20;
    --brand-blue: #3daef0;
    --brand-dark: #212428;
    --footer-text: #ffffff;
    --placeholder: #e4e6ea;
  }
  * { box-sizing: border-box; margin: 0; padding: 0; }
  html, body { width: 1200px; height: 1200px; overflow: hidden; }
  body {
    background: var(--canvas);
    font-family: "Jost", "Futura", sans-serif;
    color: var(--ink);
  }
  .letterhead {
    position: absolute;
    left: 200px; top: 34px;
    width: 800px; height: 1132px;
    background: var(--paper);
    box-shadow: 0 6px 24px rgba(0,0,0,0.12);
    overflow: hidden;
  }
  .brand {
    position: absolute; left: 76px; top: 51px;
    display: flex; align-items: center; gap: 20px;
  }
  .brand-square {
    width: 64px; height: 64px; background: var(--brand-blue);
  }
  .brand-name {
    font-family: "Montserrat", sans-serif; font-weight: 700;
    font-size: 35px; line-height: 37px; letter-spacing: 0.6px;
    color: var(--brand-dark);
  }
  .letter-date, .recipient {
    position: absolute; right: 76px; text-align: right;
    font-size: 15.8px;
  }
  .letter-date { top: 166px; }
  .recipient { top: 211px; line-height: 25.3px; font-style: normal; }
  .letter-body {
    position: absolute; left: 160px; top: 368px; width: 564px;
    font-size: 16px; line-height: 29px; text-align: justify;
  }
  .letter-body p + p { margin-top: 29px; }
  .sign-off {
    position: absolute; left: 160px; top: 838px; font-size: 15.8px;
  }
  .signature {
    position: absolute; left: 102px; top: 872px; width: 192px; height: 68px;
    background: var(--placeholder);
  }
  .signatory {
    position: absolute; left: 160px; top: 954px; font-size: 15.8px;
    text-transform: uppercase;
  }
  .contact-band {
    position: absolute; left: 0; top: 1046px; width: 800px; height: 57px;
  }
  .contact-band svg { position: absolute; inset: 0; }
  .contact-phone, .contact-web {
    position: absolute; top: 0; line-height: 57px;
    color: var(--footer-text); font-size: 14px; font-weight: 500;
  }
  .contact-phone { left: 75px; }
  .contact-web { right: 73px; text-transform: uppercase; }
</style>
</head>
<body>
  <main class="letterhead">
    <header class="brand">
      <div class="brand-square"></div>
      <div class="brand-name">FIELDLINE<br>PLANNING</div>
    </header>

    <div class="letter-date">June 09, 2023</div>

    <address class="recipient">
      Recippient Name<br>
      Vice President<br>
      Example Incooration<br>
      State
    </address>

    <section class="letter-body">
      <p>Lorem ipsum dolor sit amet, consectetur adipiscing elit. Phasellus nec velit sed ligula facilisis malesuada interdum non urna. Aliquam auctor eros sed gravida viverra. Mauris fringilla ac elit vitae laoreet. Integer condimentum vel lectus non eleifend. Quisque facilisis faucibus blandit. Proin vestibulum dapibus ipsum eu commodo. Nullam hendrerit lectus nec lectus venenatis mattis.</p>
      <p>Vestibulum ornare lorem sed feugiat faucibus. Morbi efficitur sapien ut tellus pellentesque, a lacinia nisi fermentum. Sed viverra mi lacus, ac scelerisque nisl fringilla at. Nullam lectus ipsum, laoreet ac libero eget, dapibus faucibus magna. Orci varius natoque penatibus et magnis dis parturient montes, nascetur ridiculus mus. Integer in posuere orci. Pellentesque euismod ut ante eu elementum. Ut consectetur ac urna sed varius.fringilla at.</p>
      <p>Nullam lectus ipsum, laoreet ac libero eget, dapibus faucibus magna. Orci varius natoque penatibus et magnis dis parturient montes.</p>
    </section>

    <div class="sign-off">Kinds Regards</div>
    <div class="signature" role="img" aria-label="Handwritten signature of the sender"></div>
    <div class="signatory">Dara Whitlow</div>

    <footer class="contact-band">
      <svg width="800" height="57" viewBox="0 0 800 57" aria-hidden="true">
        <rect width="800" height="57" fill="var(--brand-dark)"/>
        <path d="M0 0 H316 Q270 25 229 57 H0 Z" fill="var(--brand-blue)"/>
      </svg>
      <span class="contact-phone">(02)&nbsp; 5550 1478</span>
      <span class="contact-web">www.fieldlineplanning.com</span>
    </footer>
  </main>
</body>
</html>
```